Velvet Crest Car Detailing Brochure

I would like a trifold brochure designed for my car detailing business. The background has to be full black or mostly black with some designing using only colors present in our logo.

Front page must have our logo and name, list of services, a photo and mybe our phone number but no long text.

Inside I want to present each service one by one with its description and a photo representing/showing each service. (I will provide the text below). For photos, use stock photos and I will add come of mines already too.

On the back of the brochure I want to have contact & info: phone number, opening hours, address, website, Instagram.

Outside left I want the text About us and photo/design.

I want the brochure to be neat, professional, easy to read, but at the same time not too boring.

Text:
1. About us
a. the ultimate destination for car care in Geneva. We provide personalized, detail-oriented services that bring out the best in your car. With our expert techniques and dedicated approach, we ensure that your car receives the utmost care and attention. Experience a place where passion meets precision and let us create an exceptional car care experience designed just for you.
2. Services:

DETAILING & HAND WASH

• Comprehensive exterior & interior care
• Personalisation and tailored cleaning packages
• Decontamination
• Premium products
• Attention to detail for a perfect finish

POLISHING

• Eliminates scratches, holograms
• Revives and protects paint
• Ensures lasting gloss
• Enhances paint life
• Preserves car’s value and beauty

CERAMIC TREATMENT

• Durable paint protection
• Water-repellent (hydrophobic) effect
• Easier cleaning, enhanced shine
• Long-term surface safeguarding
• Shields against environmental impacts

DRY ICE WASH

• Innovative, waterless method
• Safe for all car parts
• Deep cleans, removes odors
• Allergen-free, antibacterial
• Gentle, effective
• Advanced cleaning technology

COVERING

• Personalized vehicle styling
• More than 150 colours available
• Clean cut without using a cutter
• High-quality, durable materials
• Custom designs available

PROTECTION FILM

• Invisible, durable shield
• Self-healing technology
• 10-year warranty by QR VONT

DETAILING BOUTIQUE

• Premium brands available
• Buy on site during your visit
• Marble Harbour, Zeb Autos, DRUP Polaro
• Essential for at-home car care
• Perfect for quick touch-ups
(for these three brands you can put their logos

Target Market(s)

Our target market includes car owners of all price ranges, with a special focus on those who are passionate about their vehicles. We cater to clients who value excellent service and results, and seek to maintain their cars in pristine condition.

Industry/Entity Type

Automobile / Car detailing

Colors

Designer to choose colors to be used in the design.

Requirements
Must have
• Brand Consistency: The brochure must adhere to our brand colors and style, particularly utilizing the colors present in our logo. Trifold Layout: The design must be specifically tailored for a trifold brochure format. Legibility: Text must be easy to read against the mostly black background, with appropriate font size and style. Professional Look and Feel: The overall design must convey professionalism while being engaging and not overly complex. Photo representation: each service description should have a phot presenting it.
Should not have
• Overcrowded Design: Avoid cluttering with too much text or too many images. The layout should be clean and easy to navigate. Cartoonish Fonts or Graphics: Avoid using unprofessional or casual fonts and graphics that do not align with the upscale and professional image of our business. Distracting Backgrounds: The background should complement and not overpower the content. Stick to the theme of mostly black with design elements from our logo.

```html
<!DOCTYPE html>
<html lang="en">
<head>
<meta charset="utf-8">
<title>Velvet Crest Car Detailing – Trifold Brochure</title>
<link rel="stylesheet" href="https://fonts.googleapis.com/css2?family=Montserrat:ital,wght@0,400;0,500;0,600;0,700;0,800;1,800&display=swap">
<style>
:root{
  --stage:#7d7d7d;
  --ink:#070707;
  --panel:#111112;
  --carbon:#161617;
  --white:#ffffff;
  --pink:#e0358f;
  --violet:#9a5fc6;
  --blue:#4f92dc;
  --brand-gradient:linear-gradient(90deg,#d9369a 0%,#a659c4 55%,#5a93da 100%);
  --font:'Montserrat',Arial,sans-serif;
}
*{box-sizing:border-box;margin:0;padding:0}
html,body{width:1163px;height:1200px;overflow:hidden;background:var(--stage)}
.canvas{position:relative;width:1163px;height:1200px;background:var(--stage);font-family:var(--font);color:var(--white)}
.spread-frame{position:absolute;left:211px;width:740px;height:572px;overflow:hidden}
.spread-frame.outside{top:18px}
.spread-frame.inside{top:610px}
.spread{position:absolute;left:0;top:0;width:870px;height:673px;transform:scale(0.85057);transform-origin:0 0;background:var(--ink);overflow:hidden}
.panel{position:absolute;top:0;height:673px;overflow:hidden}
.photo{position:absolute}

/* ---------- outside ---------- */
.about{left:0;width:287px;background:var(--ink)}
.about-title{position:absolute;left:30px;top:36px;font-size:31px;font-weight:700;color:var(--pink)}
.about-text{position:absolute;left:30px;top:92px;width:228px;font-size:12.6px;line-height:15.8px;font-weight:400}
.about .photo{left:0;top:313px;width:287px;height:360px;background:linear-gradient(180deg,#1b1c20 0%,#2a2e36 40%,#2f8fe0 62%,#1d6fc2 78%,#d7d9dc 100%)}

.contact{left:287px;width:291px}
.contact .photo{left:0;top:0;width:291px;height:673px;background:linear-gradient(180deg,#3a3b3e 0%,#1a1b1d 30%,#0c0c0d 60%,#050505 100%)}
.brand-mark{position:absolute;border-radius:50%;border:3px solid var(--violet)}
.contact .brand-mark{left:85px;top:330px;width:120px;height:120px}
.brand-name{position:absolute;text-align:center;font-weight:400;color:var(--white);letter-spacing:1px;line-height:1.08}
.contact .brand-name{left:0;width:291px;top:462px;font-size:27px}
.contact-lines{position:absolute;left:0;width:291px;text-align:center;color:var(--pink)}
.address{top:542px;font-size:12.5px;line-height:15px}
.phone{top:584px;font-size:14px;font-weight:500}
.email{top:616px;font-size:12.5px}

.cover{left:578px;width:292px;background:var(--ink)}
.cover .photo{left:0;top:150px;width:292px;height:330px;background:radial-gradient(ellipse at 60% 45%,#5a5c60 0%,#26272a 35%,#0b0b0c 70%,#050505 100%)}
.cover .brand-mark{left:21px;top:18px;width:94px;height:94px}
.cover .brand-name{left:0;width:136px;top:122px;font-size:21px}
.cover-title{position:absolute;right:13px;top:458px;text-align:right;font-size:30px;font-weight:800;line-height:31px;letter-spacing:.5px}
.cover-services{position:absolute;right:13px;top:535px;text-align:right;font-size:12.6px;font-weight:600;line-height:15.8px;white-space:pre}
.phone-band{position:absolute;left:48px;top:618px;width:244px;height:38px;background:var(--brand-gradient);clip-path:polygon(7% 0,100% 0,100% 100%,0 100%);font-size:22px;font-weight:800;font-style:italic;text-align:right;padding-right:14px;line-height:38px}

/* ---------- inside ---------- */
.inside .spread{background:var(--carbon)}
.services-left{left:0;width:293px;background:var(--carbon)}
.services-photos{left:293px;width:291px;background:var(--carbon);border-left:1px solid #262628}
.services-right{left:584px;width:286px;background:var(--carbon)}
.section-title{position:absolute;right:24px;top:52px;text-align:right;font-size:30px;font-weight:800;line-height:30px;color:var(--pink)}
.band{position:absolute;height:38px;background:var(--brand-gradient);font-size:14.5px;font-weight:700;line-height:38px;color:#101010;letter-spacing:.2px}
.services-left .band{left:34px;width:259px;clip-path:polygon(6% 0,100% 0,100% 100%,0 100%);text-align:right;padding-right:10px}
.services-right .band{left:0;width:257px;clip-path:polygon(0 0,93% 0,100% 100%,0 100%);padding-left:12px}
.bullets{position:absolute;list-style:none;font-size:10.6px;line-height:17.4px;font-weight:500}
.services-left .bullets{right:12px;text-align:right}
.services-left .bullets li::after{content:"";display:inline-block;width:7px;height:8px;margin-left:7px;background:var(--blue);clip-path:polygon(100% 0,0 50%,100% 100%)}
.services-right .bullets{left:13px}
.services-right .bullets li::before{content:"";display:inline-block;width:7px;height:8px;margin-right:8px;background:var(--blue);clip-path:polygon(0 0,100% 50%,0 100%)}
.services-photos .brand-mark{left:16px;top:32px;width:114px;height:114px}
.mark-name{position:absolute;left:16px;top:72px;width:114px;text-align:center;font-size:13px;font-weight:600;line-height:17px;color:var(--white)}
.services-photos .photo{width:144px;height:159px}
.col-a{left:1px}
.col-b{left:148px}
.row-0{top:8px}
.row-1{top:174px}
.row-2{top:340px}
.row-3{top:506px}
</style>
</head>
<body>
<main class="canvas">

  <section class="spread-frame outside" aria-label="Brochure outside">
    <div class="spread">
      <article class="panel about">
        <h2 class="about-title">About us</h2>
        <p class="about-text">The ultimate destination for car care in Geneva. We provide personalized, detail-oriented services that bring out the best in your car. With our expert techniques and dedicated approach, we ensure that your car receives the utmost care and atten-tion. Experience a place where passion meets precision and let us create an exceptional car care experience designed just for you.</p>
        <div class="photo" role="img" aria-label="Bright blue sports coupé parked in a dark garage"></div>
      </article>

      <article class="panel contact">
        <div class="photo" role="img" aria-label="Dark detailing studio with ceiling light panels"></div>
        <div class="brand-mark"></div>
        <p class="brand-name">VELVET<br>CREST</p>
        <p class="contact-lines address">Rue des Tilleuls 8,<br>1227 Carouge</p>
        <p class="contact-lines phone">+41 790 555 218</p>
        <p class="contact-lines email">mara@velvetcrest.ch</p>
      </article>

      <article class="panel cover">
        <div class="photo" role="img" aria-label="Glossy black car lit by studio light"></div>
        <div class="brand-mark"></div>
        <p class="brand-name">VELVET<br>CREST</p>
        <h1 class="cover-title">SERVICES<br>THAT SHINE</h1>
        <p class="cover-services">•Detailing &amp; Hand Wash    •Polishing
•Ceramic Treatment   •Dry Ice Wash
•Covering    •Protection Film
•Detailing Boutique</p>
        <div class="phone-band">+41 790 555 218</div>
      </article>
    </div>
  </section>

  <section class="spread-frame inside" aria-label="Brochure inside">
    <div class="spread">
      <article class="panel services-left">
        <h2 class="section-title">OUR<br>SERVICES</h2>

        <h3 class="band" style="top:175px">DETAILING &amp; HAND WASH</h3>
        <ul class="bullets" style="top:220px">
          <li>Comprehensive exterior &amp; interior care</li>
          <li>Personalisation and tailored cleaning packages</li>
          <li>Decontamination</li>
          <li>Premium products</li>
          <li>Attention to detail for a perfect finish</li>
        </ul>

        <h3 class="band" style="top:340px">POLISHING</h3>
        <ul class="bullets" style="top:386px">
          <li>durable paint protection</li>
          <li>water-repellent (hydrophobic) effect</li>
          <li>easier cleaning, enhanced shine</li>
          <li>long-term surface safeguarding</li>
          <li>shields against environmental impacts</li>
        </ul>

        <h3 class="band" style="top:506px">CERAMIC TREATMENT</h3>
        <ul class="bullets" style="top:552px">
          <li>Eliminates scratches, holograms</li>
          <li>Revives and protects paint</li>
          <li>Ensures lasting gloss</li>
          <li>Enhances paint life</li>
          <li>Preserves car’s value and beauty</li>
        </ul>
      </article>

      <div class="panel services-photos">
        <div class="brand-mark"></div>
        <p class="mark-name">VELVET<br>CREST</p>
        <div class="photo col-b row-0" style="background:linear-gradient(160deg,#c9ccd0,#6a8aa0 50%,#1f4a66)" role="img" aria-label="Hands applying coloured vinyl wrap to a car door"></div>
        <div class="photo col-a row-1" style="background:linear-gradient(160deg,#8d94a6,#4a4d55 50%,#1d1e21)" role="img" aria-label="Microfibre mitt hand washing a car wheel"></div>
        <div class="photo col-b row-1" style="background:linear-gradient(160deg,#4a4b4e,#d8dadc 55%,#9fa2a6)" role="img" aria-label="Dry ice cleaning machine releasing vapour"></div>
        <div class="photo col-a row-2" style="background:linear-gradient(160deg,#2a2b2e,#3fa9c0 45%,#d9d2c2)" role="img" aria-label="Polisher working on a masked car panel"></div>
        <div class="photo col-b row-2" style="background:linear-gradient(160deg,#bfc1c4,#55585d 50%,#151517)" role="img" aria-label="Technician applying protection film to a car"></div>
        <div class="photo col-a row-3" style="background:linear-gradient(160deg,#3c8fb0,#2a2b2e 50%,#6b6e73)" role="img" aria-label="Rotary polisher applying ceramic coating"></div>
        <div class="photo col-b row-3" style="background:linear-gradient(90deg,#3a3a3c,#4ec6d8 35%,#f0a3c4 65%,#b8d66a)" role="img" aria-label="Row of colourful car care spray bottles"></div>
      </div>

      <article class="panel services-right">
        <h3 class="band" style="top:8px">COVERING</h3>
        <ul class="bullets" style="top:54px">
          <li>Personalized vehicle styling</li>
          <li>More than 150 colours available</li>
          <li>Clean cut without using a cutter</li>
          <li>High-quality, durable materials</li>
          <li>Custom designs available</li>
        </ul>

        <h3 class="band" style="top:174px">DRY ICE WASH</h3>
        <ul class="bullets" style="top:219px">
          <li>Innovative, waterless method</li>
          <li>Safe for all car parts</li>
          <li>Deep cleans, removes odors</li>
          <li>Allergen-free, antibacterial</li>
          <li>Gentle, effective</li>
          <li>Advanced cleaning technology</li>
        </ul>

        <h3 class="band" style="top:340px">PROTECTION FILM</h3>
        <ul class="bullets" style="top:386px">
          <li>Invisible, durable shield</li>
          <li>Self-healing technology</li>
          <li>10-year warranty by QR VONT</li>
        </ul>

        <h3 class="band" style="top:506px">DETAILING BOUTIQUE</h3>
        <ul class="bullets" style="top:549px">
          <li>Premium brands available</li>
          <li>Buy on site during your visit</li>
          <li>Marble Harbour, Zeb Autos, DRUP Polaro</li>
          <li>Essential for at-home car care</li>
          <li>Perfect for quick touch-ups</li>
        </ul>
      </article>
    </div>
  </section>

</main>
</body>
</html>
```